One of a Kind Clean Business Card

We need to design a new business card template for our company. Our company designs and produced merchandising displays. You can see a sample of what we produce on our site www.qorvatfixtures.com. I have uploaded our logo in vector format, as well as a picture of our current business cards. We want a totally different look. We want simple and clean, looking forward to seeing what people create.
Updates

I would like to update the address for Tellur Display Group Inc. 418 N Brindle Ave Arlington Heights, IL 60817 Would also note. No QR codes

Industry/Entity Type

Business

Contact Information for Business Card

Need a 1 sided business card designed.

Font styles to use
Serif

Requirements
Must have
• Easy to view; Clean Design
Nice to have
• Features that promote engineering and creativity
Should not have
• Too much clutter, keep it simple

```html
<!DOCTYPE html>
<html lang="en">
<head>
<meta charset="utf-8">
<title>Tellur Display Group Inc. — Business Card</title>
<link rel="stylesheet" href="https://fonts.googleapis.com/css2?family=Open+Sans:ital,wght@0,400;0,600;0,700;1,700&display=swap">
<style>
  :root {
    --backdrop: #d9d9d9;
    --card-white: #f4f4f2;
    --panel-black: #121212;
    --accent-red: #8c1c1f;
    --ink: #1c1c1c;
    --light-text: #f2f2f2;
  }
  * { margin: 0; padding: 0; box-sizing: border-box; }
  html, body {
    width: 1200px;
    height: 800px;
    overflow: hidden;
    background: var(--backdrop);
    font-family: "Open Sans", Arial, sans-serif;
  }
  .card {
    position: absolute;
    left: 180px;
    top: 160px;
    width: 840px;
    height: 480px;
    border-radius: 30px;
    overflow: hidden;
    background: var(--card-white);
    box-shadow: 0 10px 24px rgba(0,0,0,0.18);
  }
  .card-shapes {
    position: absolute;
    inset: 0;
    width: 100%;
    height: 100%;
  }
  .brand {
    position: absolute;
    left: 60px;
    top: 170px;
    width: 360px;
  }
  .brand-name {
    font-size: 34px;
    font-weight: 600;
    line-height: 1.15;
    color: var(--accent-red);
    letter-spacing: 0.5px;
  }
  .brand-address {
    margin-top: 16px;
    font-size: 15px;
    font-weight: 400;
    color: var(--ink);
  }
  .contact {
    position: absolute;
    right: 60px;
    top: 130px;
    text-align: right;
    color: var(--light-text);
  }
  .contact-name {
    font-size: 34px;
    font-weight: 700;
    font-style: italic;
    margin-bottom: 14px;
  }
  .contact-name .surname { color: var(--accent-red); }
  .contact-line {
    font-size: 21px;
    line-height: 1.35;
  }
</style>
</head>
<body>
  <div class="card">
    <svg class="card-shapes" viewBox="0 0 840 480" aria-hidden="true">
      <polygon class="accent-band" points="408,0 430,0 540,480 518,480" fill="var(--accent-red)"/>
      <polygon class="dark-panel" points="430,0 840,0 840,480 540,480" fill="var(--panel-black)"/>
    </svg>

    <div class="brand">
      <div class="brand-name">Tellur<br>Display Group Inc.</div>
      <div class="brand-address">418 N Brindle Ave Arlington Heights, IL 60817</div>
    </div>

    <div class="contact">
      <div class="contact-name">Dale <span class="surname">Korvin</span></div>
      <div class="contact-line">815-555-0142</div>
      <div class="contact-line">312-555-0176</div>
      <div class="contact-line">dkorvin@qorvatfixtures.com</div>
      <div class="contact-line">www.qorvatfixtures.com</div>
    </div>
  </div>
</body>
</html>
```